Ridge Contracting LLC Business Card Design

I am looking for a creative and unique business card design. We are a commercial construction general contractor. With the name "RIDGE" Contracting, I am hoping to see some neat designs that correlate with the name.

```html
<!DOCTYPE html>
<html lang="en">
<head>
<meta charset="utf-8">
<title>Ridge Contracting LLC – Business Card</title>
<link href="https://fonts.googleapis.com/css2?family=Arimo:wght@400;700&family=Quicksand:wght@500;600&display=swap" rel="stylesheet">
<style>
  :root {
    --canvas: #d9d9d9;
    --card-white: #ffffff;
    --card-black: #000000;
    --brand-blue: #2f8fd6;
    --brand-blue-light: #4aa8e8;
    --rule-grey: #e2e2e2;
    --steel-grey: #b9b9b9;
    --ink: #1e1e1e;
    --muted: #6b6b6b;
  }
  * { box-sizing: border-box; margin: 0; padding: 0; }
  html, body {
    width: 1200px; height: 1166px; overflow: hidden;
    background: var(--canvas);
    font-family: "Arimo", Arial, sans-serif;
  }
  .stage {
    position: relative; width: 1200px; height: 1166px;
    display: flex; justify-content: center; align-items: center; gap: 40px;
  }
  .card {
    position: relative; width: 535px; height: 305px; overflow: hidden;
    box-shadow: 6px 8px 10px rgba(0,0,0,0.22);
  }
  /* Front */
  .card--front { background: var(--card-white); color: var(--ink); }
  .wordmark {
    font-family: "Arimo", Arial, sans-serif; font-weight: 700;
    color: var(--brand-blue); line-height: 1;
  }
  .card--front .wordmark {
    position: absolute; left: 20px; top: 52px; font-size: 30px; letter-spacing: 1px;
  }
  .card--front .wordmark small {
    display: block; font-size: 10px; letter-spacing: 4.6px; margin-top: 4px;
  }
  .holder {
    position: absolute; right: 20px; top: 80px; text-align: right;
  }
  .holder__name {
    font-family: "Quicksand", sans-serif; font-weight: 600;
    font-size: 24px; color: var(--brand-blue); line-height: 1;
  }
  .holder__role {
    font-family: "Quicksand", sans-serif; font-weight: 500;
    font-size: 12px; color: var(--muted); margin-top: 2px;
  }
  .holder-tab {
    position: absolute; right: 0; top: 79px; width: 9px; height: 45px;
    background: var(--brand-blue); border-radius: 5px 0 0 5px;
  }
  .divider {
    position: absolute; left: 19px; right: 19px; top: 136px; height: 2px;
    background: var(--rule-grey);
  }
  .contacts { position: absolute; left: 18px; top: 158px; list-style: none; font-size: 12px; }
  .contacts li { display: flex; align-items: flex-start; gap: 13px; line-height: 17px; }
  .contacts li + li { margin-top: 2px; }
  .contacts li.address { margin-bottom: 18px; }
  .contacts svg { flex: none; width: 13px; height: 13px; margin-top: 2px; }
  .accent-bar {
    position: absolute; left: 0; bottom: 0; width: 252px; height: 7px;
    background: linear-gradient(90deg, var(--brand-blue), var(--brand-blue-light));
  }
  /* Back */
  .card--back { background: var(--card-black); }
  .card--back .wordmark {
    position: absolute; left: 0; right: 0; top: 122px; text-align: center;
    font-size: 52px; letter-spacing: 3px;
  }
  .card--back .wordmark small {
    display: block; font-size: 15px; letter-spacing: 7px; margin-top: 8px;
  }
  .web {
    position: absolute; left: 0; right: 0; top: 266px; text-align: center;
    color: #ffffff; font-size: 12px; letter-spacing: 2.4px;
  }
  .band-steel { position: absolute; left: 0; right: 0; bottom: 11px; height: 4px; background: var(--steel-grey); }
  .band-blue { position: absolute; left: 0; right: 0; bottom: 0; height: 7px; background: var(--brand-blue); }
</style>
</head>
<body>
<main class="stage">
  <section class="card card--front" aria-label="Card front">
    <div class="wordmark">RIDGE<small>CONTRACTING</small></div>
    <div class="holder">
      <div class="holder__name">Corin Dalby</div>
      <div class="holder__role">Manager</div>
    </div>
    <span class="holder-tab"></span>
    <span class="divider"></span>
    <ul class="contacts">
      <li class="address">
        <svg viewBox="0 0 14 14"><path d="M7 1a4.3 4.3 0 0 0-4.3 4.3C2.7 8.5 7 13 7 13s4.3-4.5 4.3-7.7A4.3 4.3 0 0 0 7 1zm0 6a1.7 1.7 0 1 1 0-3.4A1.7 1.7 0 0 1 7 7z" fill="var(--brand-blue)"/></svg>
        <span>4870 Cedar Crest Drive, Suite 310<br>Maple Heights, OH 45021</span>
      </li>
      <li>
        <svg viewBox="0 0 14 14"><rect x="3.5" y="1" width="7" height="12" rx="1.2" fill="none" stroke="var(--brand-blue)" stroke-width="1.4"/><circle cx="7" cy="11" r="0.8" fill="var(--brand-blue)"/></svg>
        <span>555-014-2290</span>
      </li>
      <li>
        <svg viewBox="0 0 14 14"><path d="M3.2 1.5l2 2.6-1.1 1.4c.8 1.8 2.2 3.2 4 4l1.4-1.1 2.6 2-1 2c-4.8-.4-8.8-4.4-9.2-9.2z" fill="var(--brand-blue)"/></svg>
        <span>555-014-2290</span>
      </li>
      <li>
        <svg viewBox="0 0 14 14"><rect x="1" y="3" width="12" height="8.5" fill="var(--brand-blue)"/><path d="M1 3l6 5 6-5" fill="none" stroke="#fff" stroke-width="1.1"/></svg>
        <span>cdalby@ridgecontracting.com</span>
      </li>
      <li>
        <svg viewBox="0 0 14 14"><g fill="none" stroke="var(--brand-blue)" stroke-width="1.1"><circle cx="7" cy="7" r="5.6"/><ellipse cx="7" cy="7" rx="2.4" ry="5.6"/><path d="M1.4 7h11.2M2.3 4.2h9.4M2.3 9.8h9.4"/></g></svg>
        <span>www.ridgecontracting.com</span>
      </li>
    </ul>
    <span class="accent-bar"></span>
  </section>

  <section class="card card--back" aria-label="Card back">
    <div class="wordmark">RIDGE<small>CONTRACTING</small></div>
    <div class="web">www.ridgecontracting.com</div>
    <span class="band-steel"></span>
    <span class="band-blue"></span>
  </section>
</main>
</body>
</html>
```